The Circle BOLQ: Global Policy to Local Action

We need two professional visuals that represent the vision and strategy of the organization. I attached two rough images of the first visual and one image of the second visual. I also attached a pdf of the narrative to give context for each visual.

Target Market(s)

Global Health Policy Makers

Colors
ec1f27

Requirements
Must have
• Two separate images representing the flow of the work

```html
<!DOCTYPE html>
<html lang="en">
<head>
<meta charset="utf-8">
<title>The Circle BOLQ – Sustainable Development Goals</title>
<link rel="stylesheet" href="https://fonts.googleapis.com/css2?family=Montserrat:wght@500;600;700;800;900&display=swap">
<style>
  :root {
    --purple: #55286f;
    --red: #d2232a;
    --blue: #3489c9;
    --green: #7ab527;
    --orange: #fd9f0d;
    --ink: #222222;
    --line: #b8b8b8;
    --paper-top: #f4f4f4;
    --paper-mid: #e6e6e6;
  }
  * { box-sizing: border-box; margin: 0; padding: 0; }
  html, body { width: 910px; height: 1200px; overflow: hidden; }
  body {
    font-family: "Montserrat", sans-serif;
    color: var(--ink);
    background: #ffffff;
  }
  .poster {
    position: relative;
    width: 910px;
    height: 1200px;
    background: radial-gradient(ellipse at 50% 45%, var(--paper-top) 0%, var(--paper-mid) 100%);
    overflow: hidden;
  }
  .header {
    position: absolute; left: 0; top: 0; width: 100%; height: 98px;
    background: var(--purple);
    border-bottom: 8px solid var(--red);
    display: flex; align-items: center; justify-content: center;
  }
  .header h1 {
    color: #fff; font-weight: 800; font-size: 38px; letter-spacing: 0.5px;
  }
  .connectors { position: absolute; left: 0; top: 0; }
  .wheel { position: absolute; left: 192px; top: 133px; }
  .wheel text { font-family: "Montserrat", sans-serif; fill: #fff; font-weight: 700; }
  .wheel .outer-label { font-size: 10px; letter-spacing: 0.2px; }
  .wheel .outer-label-long { font-size: 9px; letter-spacing: 0; }
  .wheel .inner-label { font-size: 9.5px; letter-spacing: 0.3px; }

  .hub {
    position: absolute; left: 344px; top: 285px; width: 216px; height: 216px;
    border-radius: 50%;
    display: flex; flex-direction: column; align-items: center; justify-content: center;
    text-align: center;
  }
  .brand-name { font-size: 12px; font-weight: 600; color: #444; letter-spacing: 0.5px; margin-bottom: 12px; }
  .hub-title { font-size: 17px; font-weight: 800; color: var(--red); line-height: 1.1; }
  .hub-sub { font-size: 13.5px; font-weight: 700; color: var(--purple); line-height: 1.35; margin-top: 2px; }

  .goal {
    position: absolute; width: 146px; height: 146px; border-radius: 50%;
    background: #fff;
    box-shadow: 0 3px 10px rgba(0,0,0,0.22);
  }
  .goal-ring {
    position: absolute; inset: 10px; border-radius: 50%;
    border: 2px solid var(--accent);
    display: flex; flex-direction: column; align-items: center; justify-content: center;
    text-align: center; padding: 0 8px; gap: 6px;
  }
  .goal-icon { width: 38px; height: 34px; border-radius: 8px; background: #2b2b2b; }
  .goal-label { font-size: 10.5px; font-weight: 700; line-height: 1.25; text-transform: uppercase; color: var(--ink); }

  .pillar {
    position: absolute; width: 156px; height: 156px; border-radius: 50%;
    background: #fff;
    box-shadow: 0 3px 10px rgba(0,0,0,0.22);
  }
  .pillar-disc {
    position: absolute; inset: 11px; border-radius: 50%;
    background: var(--accent);
    display: flex; flex-direction: column; align-items: center; justify-content: center; gap: 10px;
  }
  .pillar-icon { width: 56px; height: 46px; border-radius: 10px; background: rgba(255,255,255,0.92); }
  .pillar-label { color: #fff; font-size: 11px; font-weight: 800; letter-spacing: 0.3px; }

  .footer-title {
    position: absolute; left: 0; width: 100%; top: 1139px; text-align: center;
    font-size: 22px; font-weight: 800; color: #1a1a1a;
  }
  .footer-band { position: absolute; left: 0; bottom: 3px; width: 100%; height: 19px; background: var(--red); }
</style>
</head>
<body>
<main class="poster">
  <header class="header"><h1>SUSTAINABLE DEVELOPEMENT GOALS</h1></header>

  <svg class="connectors" width="910" height="1200" viewBox="0 0 910 1200" fill="none" stroke="var(--line)" stroke-width="5">
    <line x1="95" y1="222" x2="95" y2="743"/>
    <line x1="814" y1="222" x2="814" y2="743"/>
    <line x1="95" y1="743" x2="814" y2="743"/>
    <line x1="457" y1="640" x2="457" y2="743"/>
    <line x1="457" y1="743" x2="457" y2="873"/>
    <polyline points="97,1000 97,873 804,873 804,1000"/>
    <line x1="275" y1="873" x2="275" y2="1000"/>
    <line x1="457" y1="873" x2="457" y2="1000"/>
    <line x1="630" y1="873" x2="630" y2="1000"/>
  </svg>

  <svg class="wheel" width="520" height="520" viewBox="0 0 520 520" role="group" aria-label="Health system partnership wheel">
    <defs>
      <path id="outer-from-left" d="M42,260 a218,218 0 1,1 436,0 a218,218 0 1,1 -436,0"/>
      <path id="outer-from-top" d="M260,42 a218,218 0 1,1 0,436 a218,218 0 1,1 0,-436"/>
      <path id="inner-from-top" d="M260,113 a147,147 0 1,1 0,294 a147,147 0 1,1 0,-294"/>
      <filter id="hub-shadow" x="-20%" y="-20%" width="140%" height="140%">
        <feDropShadow dx="0" dy="3" stdDeviation="5" flood-opacity="0.3"/>
      </filter>
    </defs>
    <path class="segment-red" fill="var(--red)" d="M260,260 L260,5 A255,255 0 0,1 512.5,224.5 Z"/>
    <path class="segment-purple" fill="var(--purple)" d="M260,260 L512.5,224.5 A255,255 0 0,1 424,455.3 Z"/>
    <path class="segment-orange" fill="var(--orange)" d="M260,260 L424,455.3 A255,255 0 0,1 113.7,468.9 Z"/>
    <path class="segment-green" fill="var(--green)" d="M260,260 L113.7,468.9 A255,255 0 0,1 7.5,224.5 Z"/>
    <path class="segment-blue" fill="var(--blue)" d="M260,260 L7.5,224.5 A255,255 0 0,1 260,5 Z"/>
    <circle cx="260" cy="260" r="180" fill="none" stroke="rgba(0,0,0,0.18)" stroke-width="2"/>

    <text class="outer-label"><textPath href="#outer-from-left" startOffset="12.5%" text-anchor="middle">SOCIAL INSTITUTION &amp; BUSINESS LEADERSHIP</textPath></text>
    <text class="outer-label"><textPath href="#outer-from-left" startOffset="36%" text-anchor="middle">POLITICAL LEADERSHIP</textPath></text>
    <text class="outer-label outer-label-long"><textPath href="#outer-from-left" startOffset="56%" text-anchor="middle">HEALTH, EDUCATION &amp; LABOR POLICY</textPath></text>
    <text class="outer-label"><textPath href="#outer-from-top" startOffset="50%" text-anchor="middle">SOCIAL &amp; PROFESSIONAL NETWORKS</textPath></text>
    <text class="outer-label outer-label-long"><textPath href="#outer-from-top" startOffset="69%" text-anchor="middle">COMMUNITY ORGANIZATION &amp; OWNERSHIP</textPath></text>

    <text class="inner-label"><textPath href="#inner-from-top" startOffset="90%" text-anchor="middle">MANAGEMENT</textPath></text>
    <text class="inner-label"><textPath href="#inner-from-top" startOffset="11%" text-anchor="middle">POLICY MAKING</textPath></text>
    <text class="inner-label"><textPath href="#inner-from-top" startOffset="29%" text-anchor="middle">EDUCATION &amp; RESEARCH</textPath></text>
    <text class="inner-label"><textPath href="#inner-from-top" startOffset="52%" text-anchor="middle">HEALTH WORKFORCE</textPath></text>
    <text class="inner-label"><textPath href="#inner-from-top" startOffset="74%" text-anchor="middle">COMMUNITY</textPath></text>

    <circle cx="260" cy="260" r="118" fill="#f4f4f4" filter="url(#hub-shadow)"/>
    <circle cx="260" cy="260" r="106" fill="#ffffff" stroke="#e2e2e2" stroke-width="1.5"/>
  </svg>

  <div class="hub">
    <div class="brand-name">The Circle BOLQ</div>
    <div class="hub-title">HEALTH SYSTEM</div>
    <div class="hub-sub">BASED ON<br>PEOPLE’S NEED</div>
  </div>

  <div class="goal" style="left:22px;top:149px;--accent:var(--blue)"><div class="goal-ring"><span class="goal-icon" role="img" aria-label="Light bulb with leaf icon"></span><span class="goal-label">Affordable<br>clean<br>energy</span></div></div>
  <div class="goal" style="left:22px;top:321px;--accent:var(--purple)"><div class="goal-ring"><span class="goal-icon" role="img" aria-label="Water drop icon"></span><span class="goal-label">Clean water<br>&amp; sanitation</span></div></div>
  <div class="goal" style="left:22px;top:495px;--accent:var(--red)"><div class="goal-ring"><span class="goal-icon" role="img" aria-label="Bowl of fruit and vegetables icon"></span><span class="goal-label">Availability<br>for healthy<br>food</span></div></div>
  <div class="goal" style="left:22px;top:670px;--accent:var(--purple)"><div class="goal-ring"><span class="goal-icon" role="img" aria-label="House in hand icon"></span><span class="goal-label">Affordable &amp;<br>safe housing</span></div></div>

  <div class="goal" style="left:741px;top:149px;--accent:var(--red)"><div class="goal-ring"><span class="goal-icon" role="img" aria-label="Person at laptop icon"></span><span class="goal-label">Decent work</span></div></div>
  <div class="goal" style="left:741px;top:321px;--accent:var(--green)"><div class="goal-ring"><span class="goal-icon" role="img" aria-label="Gender equality symbol icon"></span><span class="goal-label">Gender<br>equality</span></div></div>
  <div class="goal" style="left:741px;top:495px;--accent:var(--orange)"><div class="goal-ring"><span class="goal-icon" role="img" aria-label="Person reading icon"></span><span class="goal-label">Quality<br>education<br>&amp; lifelong<br>learning</span></div></div>
  <div class="goal" style="left:741px;top:670px;--accent:var(--purple)"><div class="goal-ring"><span class="goal-icon" role="img" aria-label="Stacked coins icon"></span><span class="goal-label">Adequate<br>income</span></div></div>

  <div class="goal" style="left:207px;top:670px;--accent:var(--blue)"><div class="goal-ring"><span class="goal-icon" role="img" aria-label="Target icon"></span><span class="goal-label">Recreational<br>opportunities</span></div></div>
  <div class="goal" style="left:384px;top:670px;--accent:var(--orange)"><div class="goal-ring"><span class="goal-icon" role="img" aria-label="Wheelchair icon"></span><span class="goal-label">Transportation<br>for<br>accessibility</span></div></div>
  <div class="goal" style="left:556px;top:670px;--accent:var(--red)"><div class="goal-ring"><span class="goal-icon" role="img" aria-label="Group of people icon"></span><span class="goal-label">Resilient<br>communities</span></div></div>

  <div class="pillar" style="left:19px;top:935px;--accent:var(--red)"><div class="pillar-disc"><span class="pillar-icon" role="img" aria-label="Rising chart icon"></span><span class="pillar-label">ECONOMY</span></div></div>
  <div class="pillar" style="left:197px;top:935px;--accent:var(--orange)"><div class="pillar-disc"><span class="pillar-icon" role="img" aria-label="Bridge icon"></span><span class="pillar-label">INFRASTRUCTURE</span></div></div>
  <div class="pillar" style="left:374px;top:935px;--accent:var(--green)"><div class="pillar-disc"><span class="pillar-icon" role="img" aria-label="Person silhouette icon"></span><span class="pillar-label">PEOPLE</span></div></div>
  <div class="pillar" style="left:552px;top:935px;--accent:var(--purple)"><div class="pillar-disc"><span class="pillar-icon" role="img" aria-label="Hands holding plant icon"></span><span class="pillar-label">ENVIRONMENT</span></div></div>
  <div class="pillar" style="left:733px;top:935px;--accent:var(--blue)"><div class="pillar-disc"><span class="pillar-icon" role="img" aria-label="Group of people icon"></span><span class="pillar-label">SOCIETY</span></div></div>

  <div class="footer-title">THE PARTNERSHIP DIAGRAM</div>
  <div class="footer-band"></div>
</main>
</body>
</html>
```